HR services to some of biggest Silicon Valley Tech companies needs a new website

We need a new website design probably 4-5 pages initially. Here are some websites we like the look of https://quillmarkgroup.example/ , https://www.vantrel.example/ and https://pemvio.example/ .

Target Market(s)

Silicon valley tech companies

Industry/Entity Type

HR

Coding

Coded - Design and coding required

Number of Pages Required

5+ page

Requirements
Nice to have
• any stock photos or images should show a diverse group of people. Our client base is very diverse

```html
<!DOCTYPE html>
<html lang="en">
<head>
<meta charset="utf-8">
<title>Talvora Consulting — Your Human Resources Solution</title>
<link href="https://fonts.googleapis.com/css2?family=Archivo+Black&family=Arimo:ital,wght@0,400;0,700;1,400&display=swap" rel="stylesheet">
<style>
:root{
  --yellow:#fdcb00;
  --yellow-soft:#fff4c2;
  --black:#000;
  --ink:#111;
  --body:#222;
  --muted:#777;
  --white:#fff;
  --line:#e6e6e6;
}
*{box-sizing:border-box;margin:0;padding:0}
html,body{width:1200px;height:3502px;overflow:hidden}
body{position:relative;font-family:"Arimo",Arial,sans-serif;color:var(--body);background:var(--white)}
.abs{position:absolute}
.hl{color:var(--yellow)}
.heading{font-family:"Archivo Black",Arial,sans-serif;color:var(--ink);font-size:38px;line-height:46px;font-weight:400}
.btn{position:absolute;display:flex;align-items:center;justify-content:center;background:var(--yellow);color:var(--white);font-weight:700;font-size:14px}
p{font-size:13px;line-height:16.5px}

/* hero */
.hero{position:absolute;left:0;top:0;width:1200px;height:605px;background:linear-gradient(120deg,#3a3227 0%,#6b5c48 40%,#2f2d2a 70%,#191816 100%)}
.hero-shade{position:absolute;inset:0;background:rgba(0,0,0,.35)}
.brand{position:absolute;display:flex;align-items:center;gap:8px;font-weight:700;font-size:16px;color:var(--white);letter-spacing:.5px}
.brand .mark{width:14px;height:14px;background:var(--yellow);border-radius:50%}
.nav{position:absolute;top:48px;right:280px;display:flex;gap:30px}
.nav a{color:var(--white);font-weight:700;font-size:14px;text-decoration:none}
.quote-btn{position:absolute;left:957px;top:37px;width:144px;height:42px;border:2px solid var(--yellow);color:var(--white);font-weight:700;font-size:14px;display:flex;align-items:center;justify-content:center}
.social{position:absolute;left:1072px;width:28px;height:28px;border-radius:50%;background:rgba(255,255,255,.35)}
.hero-title{position:absolute;left:0;top:242px;width:1200px;text-align:center;font-family:"Archivo Black",Arial,sans-serif;color:var(--white);font-size:41px;line-height:46px}
.hero-text{position:absolute;left:310px;top:343px;width:580px;text-align:center;color:var(--white);font-size:13px;line-height:16.5px}

/* celebrating */
.certificate-placeholder{position:absolute;left:557px;top:792px;width:144px;height:146px;background:linear-gradient(135deg,var(--yellow-soft),#ffe680)}
.feature-ico{position:absolute;width:34px;height:40px}
.feature-txt{position:absolute;width:235px;font-size:13px;line-height:16.5px}

/* stats */
.stats{position:absolute;left:0;top:1125px;width:1200px;height:279px;background:linear-gradient(100deg,#e8c21d 0%,#f0cf2a 40%,#d9b318 60%,#ecc929 100%)}
.stat{position:absolute;width:220px;text-align:center;color:var(--white)}
.stat .ring{width:87px;height:87px;margin:0 auto;border:3px solid var(--white);border-radius:50%;display:flex;align-items:center;justify-content:center}
.stat .num{font-family:"Archivo Black",Arial,sans-serif;font-size:38px;line-height:44px;margin-top:12px}
.stat .lbl{font-weight:700;font-size:14px}

/* services */
.svc{position:absolute;width:196px;height:167px;border:2px solid var(--yellow);display:flex;flex-direction:column;align-items:center;justify-content:center}
.svc.active{background:var(--yellow);color:var(--white);box-shadow:0 4px 10px rgba(0,0,0,.15)}
.svc h4{font-family:"Archivo Black",Arial,sans-serif;font-size:19px;font-weight:400;margin-top:8px}
.svc p{font-size:13px;text-align:center}

/* process */
.step{position:absolute;left:181px;width:386px;height:94px;background:var(--white);border-radius:10px;box-shadow:0 3px 14px rgba(0,0,0,.1);padding:16px 0 0 35px}
.step h5{font-size:15px;font-weight:700;color:var(--ink);margin-bottom:5px}
.step-num{position:absolute;left:-15px;top:32px;width:28px;height:28px;border-radius:50%;background:var(--white);box-shadow:0 1px 6px rgba(0,0,0,.12);color:var(--yellow);font-size:13px;display:flex;align-items:center;justify-content:center}

/* testimonials */
.testi-bg{position:absolute;left:0;top:2335px;width:1200px;height:499px;background:linear-gradient(90deg,#2a2a2a 0%,#3a332c 55%,#6a4a2c 80%,#3a2a1e 100%)}
.testi-card{position:absolute;left:0;top:2452px;width:784px;height:263px;background:var(--white)}
.stars{color:var(--yellow);font-size:26px;letter-spacing:10px}

/* footer */
.footer{position:absolute;left:0;top:3126px;width:1200px;height:340px;background:var(--black)}
.fcol{position:absolute;top:3180px}
.fcol h6{font-family:"Archivo Black",Arial,sans-serif;font-size:19px;font-weight:400;color:var(--white);margin-bottom:8px}
.fcol a{display:block;color:#666;font-size:13px;line-height:16.5px;text-decoration:none}
.bottom-bar{position:absolute;left:0;top:3466px;width:1200px;height:36px;background:var(--yellow);display:flex;align-items:center;justify-content:center;font-size:13px;color:var(--ink)}
</style>
</head>
<body>

<!-- Hero -->
<section class="hero" role="img" aria-label="Photo of two business people in conversation at a table in a bright office">
  <div class="hero-shade"></div>
</section>
<div class="brand" style="left:99px;top:60px"><span class="mark"></span>Talvora Consulting</div>
<nav class="nav">
  <a href="#">Home</a><a href="#">How it works</a><a href="#">About</a><a href="#">Services</a><a href="#">Blog</a>
</nav>
<div class="quote-btn">Get a free quote</div>
<span class="social" style="top:213px" aria-label="Social link"></span>
<span class="social" style="top:278px" aria-label="Social link"></span>
<span class="social" style="top:342px" aria-label="Social link"></span>
<h1 class="hero-title">Your <span class="hl">Human</span><br><span class="hl">Resources</span> Solution</h1>
<p class="hero-text">Lorem ipsum dolor sit amet, consectetur adipiscing elit, sed do eiusmod tempor incididunt ut labore et dolore magna aliqua. Quis ipsum suspendisse ultrices gravida. Risus commodo viverra maecenas accumsan lacus vel facilisis. maecenas accumsan lacus vel facilisis. maecenas accumsan lacus vel facilisis. maecenas accumsan lacus vel facilisis.</p>
<div class="btn" style="left:530px;top:439px;width:140px;height:43px">Contact us</div>

<!-- Celebrating -->
<h2 class="heading abs" style="left:99px;top:667px">We're celebrating<br><span class="hl">15 years,</span> in<br>business!</h2>
<p class="abs" style="left:99px;top:817px;width:400px">Lorem ipsum dolor sit amet, consectetur adipiscing elit, sed do eiusmod tempor incididunt ut labore et dolore magna aliqua. Quis ipsum suspendisse ultrices gravida. Risus commodo viverra maecenas accumsan lacus vel facilisis. Lorem ipsum dolor sit amet, consectetur adipiscing elit, sed do eiusmod tempor incididunt ut labore et dolore magna aliqua. Quis ipsum suspendisse ultrices gravida. Risus commodo viverra maecenas accumsan lacus vel facilisis. Lorem ipsum dolor sit amet,</p>
<p class="abs" style="left:557px;top:673px;width:540px">Lorem ipsum dolor sit amet, consectetur adipiscing elit, sed do eiusmod tempor incididunt ut labore et dolore magna aliqua. Quis ipsum suspendisse ultrices gravida. Risus commodo viverra maecenas accumsan lacus vel facilisis. Lorem ipsum dolor sit amet, consectetur adipiscing elit, sed do eiusmod tempor incididunt ut labore et dolore magna aliqua. Quis ipsum suspendisse ultrices gravida. Risus commodo viverra maecenas accumsan lacus vel facilisis. Lorem ipsum dolor sit amet, consectetur adipiscing elit, sed do eiusmod</p>
<div class="certificate-placeholder" role="img" aria-label="Illustration of a certificate scroll with an award badge"></div>
<p class="abs" style="left:727px;top:784px;width:375px">Lorem ipsum dolor sit amet, consectetur adipiscing elit, sed do eiusmod tempor incididunt ut labore et dolore magna aliqua. Quis ipsum suspendisse ultrices gravida. Risus commodo viverra maecenas accumsan lacus vel facilisis. Lorem ipsum dolor sit amet, consectetur adipi scing elit, sed do eiusmod tempor incididunt ut labore et dolore magna aliqua. Quis ipsum suspendisse ultrices gravida. Risus commodo viverra maecenas accumsan lacus vel facilisis. Lorem ipsum dolor sit amet, consectetur adipiscing elit, sed do eiusmod tempor incididunt ut labore et dolore</p>

<svg class="feature-ico" style="left:97px;top:1012px" viewBox="0 0 34 40" fill="none" stroke="#fdcb00" stroke-width="2.5"><circle cx="17" cy="14" r="12"/><circle cx="17" cy="14" r="6"/><path d="M10 24l-5 13 6-2 3 4 3-8M24 24l5 13-6-2-3 4-3-8"/></svg>
<p class="feature-txt" style="left:150px;top:992px">We have worked with some of the most innovative companies in Silicon Valley, across a board range of industries, and we're proud to grow our client list every year</p>
<svg class="feature-ico" style="left:460px;top:1012px" viewBox="0 0 34 40" fill="none" stroke="#fdcb00" stroke-width="2.5"><circle cx="17" cy="14" r="12"/><circle cx="17" cy="14" r="6"/><path d="M10 24l-5 13 6-2 3 4 3-8M24 24l5 13-6-2-3 4-3-8"/></svg>
<p class="feature-txt" style="left:514px;top:1000px">Talvora's experienced professionals help implement and their maintain best practices allowing our clients to focus on their core competencies</p>
<svg class="feature-ico" style="left:823px;top:1012px" viewBox="0 0 34 40" fill="none" stroke="#fdcb00" stroke-width="2.5"><circle cx="17" cy="14" r="12"/><circle cx="17" cy="14" r="6"/><path d="M10 24l-5 13 6-2 3 4 3-8M24 24l5 13-6-2-3 4-3-8"/></svg>
<p class="feature-txt" style="left:877px;top:1000px">For 15 years our team of industry experts has been providing HR consulting services with innovative strategies and a partnership mentality</p>

<!-- Stats -->
<section class="stats" role="img" aria-label="Yellow-toned photo of two people shaking hands"></section>
<div class="stat" style="left:140px;top:1183px"><div class="ring"><svg width="40" height="40" viewBox="0 0 40 40" fill="#fff"><circle cx="22" cy="8" r="5"/><path d="M14 16h14l-3 10h-9zM4 30h10l8 4 12-6 2 3-14 8-16-3z"/></svg></div><div class="num">1388</div><div class="lbl">Company we help</div></div>
<div class="stat" style="left:363px;top:1183px"><div class="ring"><svg width="40" height="40" viewBox="0 0 40 40" fill="#fff"><rect x="6" y="8" width="28" height="26" rx="2"/><rect x="10" y="4" width="3" height="8"/><rect x="27" y="4" width="3" height="8"/></svg></div><div class="num">575</div><div class="lbl">Training courses</div></div>
<div class="stat" style="left:595px;top:1183px"><div class="ring"><svg width="40" height="40" viewBox="0 0 40 40" fill="#fff"><rect x="5" y="12" width="30" height="22" rx="3"/><path d="M14 12V7h12v5h-3V9h-6v3z"/></svg></div><div class="num">147</div><div class="lbl">Corporate programs</div></div>
<div class="stat" style="left:848px;top:1183px"><div class="ring"><svg width="40" height="40" viewBox="0 0 40 40" fill="#fff"><circle cx="20" cy="12" r="8"/><path d="M6 36c0-10 6-14 14-14s14 4 14 14z"/></svg></div><div class="num">301</div><div class="lbl">Our strategic partners</div></div>

<!-- Services -->
<h2 class="heading abs" style="left:129px;top:1468px">Our <span class="hl">Services</span></h2>
<p class="abs" style="left:129px;top:1525px;width:430px">Lorem ipsum dolor sit amet, consectetur adipiscing elit, sed do eiusmod tempor incididunt ut labore et dolore magna aliqua. Quis ipsum suspendisse ultrices gravida. Risus commodo viverra maecenas accumsan lacus vel facilisis. Lorem ipsum dolor sit amet, consectetur adipiscing elit, sed do eiusmod tempor incididunt ut labore et dolore magna aliqua. Quis ipsum suspendisse ultrices gravida. Risus commodo viverra erra maecenas accumsan lacus vel facilisis. Lorem ipsum dolor sit amet, consectetur adipiscing elit, sed do eiusmod tempor incididunt ut labore et dolore magna aliqua. Quis ipsum suspendisse ultrices gravida. Risus commodo viverra maecenas accumsan lacus vel facilisis. Lorem ipsum dolor sit amet, consectetur adipiscing elit, sed do eiusmod tempor incididunt ut labore et dolore magna aliqua. Quis ipsum suspendisse ultrices gravida. Risus commodo viverra maecenas accumsan lacus vel facilisis.</p>
<div class="btn" style="left:129px;top:1795px;width:235px;height:44px">Take a look at the details</div>

<div class="svc active" style="left:639px;top:1469px">
  <svg class="abs" style="right:16px;top:16px" width="20" height="20" viewBox="0 0 20 20" fill="none" stroke="#fff" stroke-width="2"><path d="M11 3h6v6M17 3l-8 8M14 12v5H3V6h5"/></svg>
  <svg width="48" height="48" viewBox="0 0 48 48" fill="#fff"><circle cx="18" cy="18" r="10"/><circle cx="33" cy="32" r="8"/><circle cx="18" cy="18" r="4" fill="#fdcb00"/><circle cx="33" cy="32" r="3" fill="#fdcb00"/></svg>
  <h4>Set up</h4>
  <p>Lorem ipsum dolor<br>sit amet, consectetur</p>
</div>
<div class="svc" style="left:875px;top:1469px">
  <svg width="54" height="54" viewBox="0 0 54 54" fill="#fdcb00"><circle cx="27" cy="8" r="5"/><rect x="22" y="14" width="10" height="8"/><rect x="26" y="22" width="2" height="8"/><rect x="10" y="28" width="34" height="2"/><circle cx="11" cy="38" r="4"/><circle cx="27" cy="38" r="4"/><circle cx="43" cy="38" r="4"/><rect x="6" y="43" width="10" height="8"/><rect x="22" y="43" width="10" height="8"/><rect x="38" y="43" width="10" height="8"/></svg>
</div>
<div class="svc" style="left:639px;top:1681px">
  <svg width="54" height="54" viewBox="0 0 54 54" fill="none" stroke="#fdcb00" stroke-width="5"><path d="M27 6a21 21 0 0 1 19 12M48 27a21 21 0 0 1-12 19M27 48a21 21 0 0 1-19-12M6 27A21 21 0 0 1 18 8"/><path d="M19 22h16M19 27h16M19 32h16" stroke-width="3"/></svg>
</div>
<div class="svc" style="left:875px;top:1681px">
  <svg width="56" height="54" viewBox="0 0 56 54" fill="#fdcb00"><rect x="14" y="4" width="28" height="16" rx="2"/><circle cx="10" cy="24" r="5"/><circle cx="28" cy="30" r="5"/><circle cx="46" cy="24" r="5"/><path d="M2 42c0-8 16-8 16 0zM38 42c0-8 16-8 16 0zM18 50c0-10 20-10 20 0z"/></svg>
</div>

<!-- Process -->
<div class="step" style="top:1935px"><span class="step-num">1</span><h5>Various versions</h5><p>Lorem ipsum dolor sit amet, consectetur adipiscing elit, sed do eiusmod tempor incididunt ut labore et</p></div>
<div class="step" style="top:2052px"><span class="step-num">2</span><h5>Various versions</h5><p>Lorem ipsum dolor sit amet, consectetur adipiscing elit, sed do eiusmod tempor incididunt ut labore et</p></div>
<div class="step" style="top:2169px"><span class="step-num">3</span><h5>Various versions</h5><p>Lorem ipsum dolor sit amet, consectetur adipiscing elit, sed do eiusmod tempor incididunt ut labore et</p></div>
<h2 class="heading abs" style="left:641px;top:1948px">Our <span class="hl">work</span> process</h2>
<div class="abs" style="left:641px;top:2005px;width:372px">
  <p>Lorem ipsum dolor sit amet, consectetur adipiscing elit, sed do eiusmod tempor incididunt ut labore et dolore magna aliqua. Quis ipsum suspendisse ultrices gravida. Risus commodo viverra maecenas accumsan lacus vel facilisis.</p>
  <p style="margin-top:8px">Lorem ipsum dolor sit amet, consectetur adipiscing elit, sed do eiusmod tempor incididunt ut labore et dolore magna aliqua. Quis ipsum suspendisse ultrices gravida. Risus commodo viverra maecenas accumsan lacus vel facilisis Lorem ipsum dolor sit amet, consectetur adipiscing elit, sed do</p>
  <p style="margin-top:14px">Lorem ipsum dolor sit amet, consectetur adipiscing elit, sed do eiusmod tempor incididunt ut labore et dolore magna aliqua. Quis ipsum suspendisse ultrices gravida. Risus commodo viverra maecenas accumsan lacus vel facilisis.</p>
</div>

<!-- Testimonials -->
<section class="testi-bg" role="img" aria-label="Dark-toned photo of a smiling client in a warm orange sweater"></section>
<div class="testi-card"></div>
<div class="abs" style="left:803px;top:2452px;width:6px;height:263px;background:var(--yellow)"></div>
<h2 class="heading abs" style="left:836px;top:2540px;color:var(--white)">Client<br><span class="hl">Testimonials</span></h2>
<svg class="abs" style="left:99px;top:2550px" width="64" height="64" viewBox="0 0 64 64"><circle cx="32" cy="32" r="32" fill="#777"/><circle cx="32" cy="25" r="11" fill="#fff"/><path d="M12 52c4-12 36-12 40 0a28 28 0 0 1-40 0z" fill="#fff"/></svg>
<div class="abs" style="left:183px;top:2558px;font-weight:700;font-size:19px;color:#666">Marcus Ellery</div>
<div class="abs stars" style="left:183px;top:2580px">★★★★</div>
<p class="abs" style="left:371px;top:2536px;width:370px;font-style:italic;color:#888;line-height:24px"><span class="hl" style="font-size:18px">“</span> Lorem ipsum dolor sit amet, consectetur adipiscing elit, sed do eiusmod tempor incididunt ut labore et dolore magna aliqua. Quis ipsum suspendisse ultrices gravida. Risus commodo viverra maecenas accumsan lacus vel facilisis.<span class="hl" style="font-size:18px">”</span></p>
<svg class="abs" style="left:716px;top:2652px" width="36" height="36" viewBox="0 0 36 36" fill="none" stroke="#444" stroke-width="2"><path d="M2 9h32M27 2l7 7-7 7M34 27H2M9 20l-7 7 7 7"/></svg>

<!-- Contact -->
<h2 class="heading abs" style="left:0;top:2888px;width:1200px;text-align:center">Need help? <span class="hl">talk with us!</span></h2>
<p class="abs" style="left:260px;top:2956px;width:680px;text-align:center;color:#777">Lorem ipsum dolor sit amet, consectetur adipiscing elit, sed do eiusmod tempor incididunt ut labore et dolore magna aliqua. Quis ipsum suspendisse ultrices gravida. Risus commodo viverra maecenas accumsan lacus vel</p>
<div class="btn" style="left:489px;top:3010px;width:222px;height:49px;color:var(--ink)">Call now (+91 555 0142)</div>

<!-- Footer -->
<footer class="footer"></footer>
<div class="brand" style="left:99px;top:3210px"><span class="mark"></span>Talvora Consulting</div>
<div class="fcol" style="left:295px"><h6>Quick links</h6><a>Home</a><a>How it works</a><a>About</a><a>Services</a><a>Blog</a></div>
<div class="fcol" style="left:485px"><h6>Helpfull links</h6><a>Privacy &amp; poliy</a><a>Terms of use</a><a>Account poicy</a><a>Cookies</a></div>
<div class="fcol" style="left:693px"><h6>Support</h6><a>Cart</a><a>Log in</a><a>Meet our team</a><a>Blog</a><a>Customer care</a></div>
<div class="abs" style="left:860px;top:3176px;color:var(--white);font-size:13px">Newsletter subscription</div>
<div class="abs" style="left:860px;top:3205px;width:195px;height:36px;border:1px solid #444;color:#666;font-size:13px;padding:10px 12px">enter you email here....</div>
<div class="abs" style="left:1064px;top:3205px;width:37px;height:36px;background:var(--yellow);display:flex;align-items:center;justify-content:center"><svg width="18" height="18" viewBox="0 0 18 18" fill="#000"><path d="M1 8l16-7-6 16-3-6z"/></svg></div>
<p class="abs" style="left:99px;top:3353px;width:730px;color:#777">Lorem ipsum dolor sit amet, consectetur adipiscing elit, sed do eiusmod tempor incididunt ut labore et dolore magna aliqua. Quis ipsum suspendisse ultrices gravida. Risus commodo viverra mae cenas accumsan lacus vel facilisis. Lorem ipsum dolor sit amet, consectetur adipiscing elit, sed do eiusmod tempor incididunt ut labore et dolore magna aliqua. Quis ipsum suspendisse ultrices gravida. Risus commodo viverra maecenas accumsan lacus vel facilisis. Lorem ipsum dolor sit amet, consectetur adipiscing elit, sed do</p>
<div class="abs" style="left:1069px;top:3452px;width:32px;height:34px;background:var(--yellow);display:flex;align-items:center;justify-content:center;z-index:2"><svg width="14" height="14" viewBox="0 0 14 14" fill="none" stroke="#000" stroke-width="2"><path d="M2 7l5-5 5 5M2 12l5-5 5 5"/></svg></div>
<div class="bottom-bar">© 2016 To 2021 TALVORA CONSULTING. All rights reserved.</div>

</body>
</html>
```